Professional and creatice Life Coach - Business Card design

I just relaunched my website and now i a need a correspoonding business card for my task as life coach. My website is www.tbalrond.com as reference. The compass is kind of a symbol for my work, as I help people navigate through their challenging phases in life. The business card should be colorful, but not too playful as I also adress business people. So it sould be creative, but professional (also to suport my other business as Management Consultant)

Target Market(s)

People who want to get teir problems resolved, in business, partnership and other personal realms

Industry/Entity Type

Life Coaching

Contact Information for Business Card

Front side should include Name, Phone number, Email, Website and address

Font styles to use
Sans Serif

Colors
add136

Requirements
Must have
• "Mag. Leopold Brantner" -> Name
"Energetische Praxis" -> Jobtitle (describing my profession as life coach)
colours and style should match my website www.tbalrond.com
Nice to have
• a compass as a symbol

```html
<!DOCTYPE html>
<html lang="de">
<head>
<meta charset="utf-8">
<title>Leopold Brantner – Business Card</title>
<link href="https://fonts.googleapis.com/css2?family=Montserrat:wght@500;700&display=swap" rel="stylesheet">
<style>
  :root {
    --stage: #3a3c40;
    --card: #262628;
    --lime: #add136;
    --white: #ffffff;
    --ink: #262628;
  }
  * { box-sizing: border-box; margin: 0; padding: 0; }
  html, body {
    width: 1200px; height: 900px; overflow: hidden;
    background: var(--stage);
    font-family: "Montserrat", Arial, sans-serif;
  }
  .canvas {
    position: relative; width: 1200px; height: 900px;
    display: flex; flex-direction: column; align-items: center; justify-content: center; gap: 50px;
  }
  .card {
    position: relative; width: 600px; height: 343px;
    background: var(--card); border-radius: 20px; overflow: hidden;
    box-shadow: 0 14px 30px rgba(0,0,0,.35);
  }
  /* Back side */
  .card-back .brand {
    position: absolute; left: 0; right: 0; top: 120px;
    display: flex; align-items: center; justify-content: center; gap: 14px;
  }
  .brand-dot { width: 34px; height: 34px; border-radius: 50%; background: var(--lime); }
  .brand-name { color: var(--lime); font-weight: 700; font-size: 30px; letter-spacing: .5px; }
  .card-back .back-web {
    position: absolute; left: 0; right: 0; bottom: 44px; text-align: center;
    color: var(--lime); font-weight: 700; font-size: 15px; letter-spacing: .3px;
  }
  /* Front side */
  .accent-stripe { position: absolute; left: 0; top: 0; bottom: 0; width: 20px; background: var(--lime); }
  .card-front .brand {
    position: absolute; left: 50px; top: 150px;
    display: flex; align-items: center; gap: 10px;
  }
  .card-front .brand-dot { width: 26px; height: 26px; }
  .card-front .brand-name { font-size: 21px; }
  .divider { position: absolute; left: 296px; top: 62px; width: 3px; height: 220px; background: var(--lime); }
  .details { position: absolute; left: 318px; top: 62px; }
  .person-name { color: var(--lime); font-weight: 700; font-size: 20px; line-height: 1.2; }
  .person-title { color: var(--white); font-weight: 700; font-size: 14px; margin-top: 4px; }
  .contact-list { list-style: none; margin-top: 28px; }
  .contact-item {
    display: flex; align-items: center; gap: 10px;
    color: var(--white); font-weight: 500; font-size: 13px; margin-bottom: 12px;
  }
  .contact-icon {
    width: 24px; height: 24px; border-radius: 50%; background: var(--lime);
    display: flex; align-items: center; justify-content: center; flex-shrink: 0;
  }
  .contact-icon svg { width: 14px; height: 14px; fill: none; stroke: var(--ink); stroke-width: 1.8; stroke-linecap: round; stroke-linejoin: round; }
</style>
</head>
<body>
<main class="canvas">
  <section class="card card-back" aria-label="Card back">
    <div class="brand"><span class="brand-dot"></span><span class="brand-name">Leopold Brantner</span></div>
    <p class="back-web">www.tbalrond.com</p>
  </section>

  <section class="card card-front" aria-label="Card front">
    <div class="accent-stripe"></div>
    <div class="brand"><span class="brand-dot"></span><span class="brand-name">Leopold Brantner</span></div>
    <div class="divider"></div>
    <div class="details">
      <h1 class="person-name">Mag. Leopold Brantner</h1>
      <p class="person-title">Energetische Praxis</p>
      <ul class="contact-list">
        <li class="contact-item">
          <span class="contact-icon"><svg viewBox="0 0 24 24"><path d="M5 3h4l2 5-2.5 1.5a11 11 0 0 0 6 6L16 13l5 2v4a2 2 0 0 1-2 2A16 16 0 0 1 3 5a2 2 0 0 1 2-2z"/></svg></span>
          +43 660 4187352
        </li>
        <li class="contact-item">
          <span class="contact-icon"><svg viewBox="0 0 24 24"><rect x="3" y="5" width="18" height="14" rx="2"/><path d="M3 7l9 6 9-6"/></svg></span>
          leopold@tbalrond.one
        </li>
        <li class="contact-item">
          <span class="contact-icon"><svg viewBox="0 0 24 24"><circle cx="12" cy="12" r="9"/><path d="M3 12h18M12 3a14 14 0 0 1 0 18M12 3a14 14 0 0 0 0 18"/></svg></span>
          www.tbalrond.com
        </li>
        <li class="contact-item">
          <span class="contact-icon"><svg viewBox="0 0 24 24"><path d="M12 21s-7-7-7-12a7 7 0 0 1 14 0c0 5-7 12-7 12z"/><circle cx="12" cy="9" r="2.5"/></svg></span>
          Lindenweg 14, 5020 Feldach, Austria
        </li>
      </ul>
    </div>
  </section>
</main>
</body>
</html>
```